Business card for Bio pharmaceutical company

Hello,
We are a bio pharmaceutical contract manufacturing company in Brisbane, Australia. Can you please create a new business card design. Please go to our website for colours http://www.velocrine.com.au.
On the back can you include the cartoon mascot Tobin Wuzzle and the tagline
"A Global Biopharmaceutical Contract Development Manufacturing Company"
Target Market(s)
Biotechnology
Industry/Entity Type
Pharmaceutical
Contact Information for Business Card
Maria Hollingby
Business Development Manager
maria.hollingby@velocrine.com.au
1947 Kelmott Street Parvale Queesnland 4213 Australia
T: +61 7 3590 2481
M +61 427 516 093
F +61 7 3648 2057
www.velocrine.com.au
Look and feel

```html
<!DOCTYPE html>
<html lang="en">
<head>
<meta charset="utf-8">
<title>Velocrine Business Card</title>
<link rel="stylesheet" href="https://fonts.googleapis.com/css2?family=Ubuntu:wght@400;500;700&display=swap">
<style>
  :root {
    --lime: #bacc55;
    --navy: #0f3352;
    --sky: #4c9dc9;
    --rule: #c9c9c9;
    --paper: #ffffff;
  }
  * { margin: 0; padding: 0; box-sizing: border-box; }
  html, body { width: 978px; height: 1200px; overflow: hidden; }
  body {
    background: var(--lime);
    font-family: "Ubuntu", sans-serif;
    position: relative;
  }
  .card {
    position: absolute;
    left: 33px;
    width: 910px;
    background: var(--paper);
    box-shadow: 0 3px 8px rgba(0,0,0,0.25);
  }
  .card-front { top: 37px; height: 536px; }
  .card-back { top: 620px; height: 538px; }

  .brand {
    position: absolute;
    left: 150px;
    top: 128px;
    display: flex;
    align-items: flex-start;
    gap: 22px;
  }
  .brand-name {
    font-size: 104px;
    font-weight: 500;
    color: var(--navy);
    letter-spacing: -1px;
    line-height: 1;
  }
  .brand-mark {
    width: 60px; height: 60px;
    background: var(--lime);
    margin-top: -58px;
  }
  .front-rule {
    position: absolute; left: 0; right: 0; top: 313px;
    border-top: 1.5px solid var(--rule);
  }
  .service {
    position: absolute;
    width: 419px; height: 75px;
    background: var(--lime);
    color: var(--navy);
    font-size: 35px;
    font-weight: 700;
    display: flex; align-items: center; justify-content: center;
  }
  .service-1 { left: 27px; top: 341px; }
  .service-2 { left: 464px; top: 341px; }
  .service-3 { left: 27px; top: 433px; }
  .service-4 { left: 464px; top: 433px; }

  .mascot {
    position: absolute; left: 70px; top: 42px;
    width: 300px; height: 350px;
  }
  .back-brand {
    position: absolute; left: 78px; top: 398px;
    display: flex; align-items: center; gap: 10px;
  }
  .back-brand-name {
    font-size: 36px; font-weight: 500; color: var(--navy);
  }
  .back-brand-mark { width: 22px; height: 22px; background: var(--lime); margin-top: -28px; }
  .tagline-art {
    position: absolute; left: 45px; top: 448px;
    width: 300px; height: 58px;
    background: #3b4a6b; opacity: 0.85; border-radius: 6px;
  }

  .contact {
    position: absolute; right: 38px;
    text-align: right;
  }
  .person-name {
    top: 22px;
    font-size: 60px; font-weight: 400; color: var(--sky);
    text-decoration: underline; text-decoration-thickness: 2px;
    text-underline-offset: 4px; line-height: 1.1;
  }
  .person-role { top: 90px; font-size: 29px; color: var(--navy); }
  .person-email { top: 128px; font-size: 23px; color: var(--lime); }
  .back-rule {
    position: absolute; left: 370px; right: 0;
    border-top: 1.5px solid var(--rule);
  }
  .back-rule-1 { top: 180px; }
  .back-rule-2 { top: 408px; }
  .address { top: 200px; font-size: 26px; color: var(--navy); line-height: 36px; }
  .phones { top: 273px; font-size: 27px; color: var(--sky); line-height: 39.5px; letter-spacing: 0.5px; }
  .website {
    position: absolute; left: 453px; top: 436px;
    width: 419px; height: 75px;
    background: var(--lime); color: var(--paper);
    font-size: 25px;
    display: flex; align-items: center; justify-content: center;
    text-decoration: none;
  }
</style>
</head>
<body>
  <section class="card card-front">
    <div class="brand">
      <span class="brand-name">Velocrine</span>
      <span class="brand-mark"></span>
    </div>
    <div class="front-rule"></div>
    <div class="service service-1">Bioharmaceutical</div>
    <div class="service service-2">Chemical Synthesis</div>
    <div class="service service-3">Microbial Products</div>
    <div class="service service-4">Vaccines</div>
  </section>

  <section class="card card-back">
    <svg class="mascot" role="img" aria-label="Cartoon bacterium mascot Tobin Wuzzle holding a cocktail glass" viewBox="0 0 300 350">
      <defs>
        <linearGradient id="mascot-tone" x1="0" y1="0" x2="1" y2="1">
          <stop offset="0" stop-color="#a9d2ee"/>
          <stop offset="1" stop-color="#5b9fd3"/>
        </linearGradient>
      </defs>
      <rect x="0" y="0" width="300" height="350" rx="40" fill="url(#mascot-tone)"/>
    </svg>
    <div class="back-brand">
      <span class="back-brand-name">Velocrine</span>
      <span class="back-brand-mark"></span>
    </div>
    <div class="tagline-art" role="img" aria-label="Hand-lettered tagline"></div>

    <div class="contact person-name">Maria Hollingby</div>
    <div class="contact person-role">Business Development Manager</div>
    <div class="contact person-email">maria.hollingby@velocrine.com.au</div>
    <div class="back-rule back-rule-1"></div>
    <div class="contact address">1947 Kelmott Street<br>Parvale Queesnland 4213 Australia</div>
    <div class="contact phones">T: +61 7 3590 2481<br>M: +61 427 516 093<br>F: +61 7 3648 2057</div>
    <div class="back-rule back-rule-2"></div>
    <a class="website" href="http://www.velocrine.com.au">www.velocrine.com.au</a>
  </section>
</body>
</html>
```